Chartered Professional Accounting Firm Needs a Business Card Design

We need a card design for an accounting firm based in Toronto, Ontario. The firm name is Leo Dart Professional Corporation. The owner of the firm is a chartered professional accountant and a certified general accountant. Services of the firm include 60% tax preparation and consulting and 40% financial statements for corporation year-end. We would like a modern design. The color could be black, white, gray, blue or other color to bring more confidence to clients. The logo of the firm should be included in the design. Thanks

Name: Leo Dart, CPA, CGA Address: 47 Amberfield Cres. Richmond Hill, ON M3K 7P2 Telephone: (416) 555-0137 Fax:(416) 555-0192 Email: leo@leodart.example

Accounting

```html
<!DOCTYPE html>
<html lang="en">
<head>
<meta charset="utf-8">
<title>Leo Dart Professional Corporation – Business Card</title>
<link rel="stylesheet" href="https://fonts.googleapis.com/css2?family=Arimo:wght@400;700&family=Cinzel:wght@700&display=swap">
<style>
  :root {
    --page: #e9e9ec;
    --card: #ffffff;
    --blue: #2e3596;
    --blue-faint: #b9b8dc;
    --gray: #8a8b90;
    --gray-light: #d6d6d8;
    --ink: #3a3a3f;
  }
  * { box-sizing: border-box; margin: 0; padding: 0; }
  html, body { width: 1200px; height: 800px; overflow: hidden; background: var(--page); }
  .card {
    position: absolute; left: 75px; top: 100px;
    width: 1050px; height: 600px;
    background: var(--card);
    box-shadow: 0 10px 30px rgba(0,0,0,.18);
    overflow: hidden;
    font-family: "Arimo", Arial, sans-serif;
  }
  .card-bands { position: absolute; inset: 0; }
  .faint-mark {
    position: absolute; left: 95px; top: 195px;
    display: flex; align-items: center; gap: 18px;
  }
  .faint-mark .square { width: 230px; height: 230px; background: var(--blue-faint); opacity: .7; }
  .faint-mark .name {
    font-family: "Cinzel", Georgia, serif; font-weight: 700;
    font-size: 40px; color: var(--blue-faint); opacity: .8; line-height: 1.1;
  }
  .firm {
    position: absolute; left: 540px; top: 60px;
    display: flex; align-items: center; gap: 18px;
  }
  .firm .circle { width: 96px; height: 96px; border-radius: 50%; background: var(--blue); flex: none; }
  .firm .firm-name {
    font-family: "Cinzel", Georgia, serif; font-weight: 700;
    color: var(--blue); font-size: 34px; line-height: 1.05;
  }
  .firm .firm-name small { display: block; font-size: 17px; letter-spacing: .5px; }
  .credentials {
    margin-top: 6px; font-size: 12px; letter-spacing: 1.2px;
    color: var(--gray); text-transform: uppercase; line-height: 1.35;
  }
  .person { position: absolute; right: 70px; top: 200px; text-align: right; }
  .person .person-name { font-weight: 700; font-size: 28px; color: var(--blue); letter-spacing: .5px; }
  .person .person-title { font-size: 15px; color: var(--blue); }
  .contacts { position: absolute; right: 70px; top: 285px; list-style: none; text-align: right; }
  .contacts li {
    display: flex; justify-content: flex-end; align-items: center; gap: 16px;
    font-size: 22px; color: var(--ink); height: 42px;
  }
  .contacts svg { width: 26px; height: 22px; fill: var(--blue); flex: none; }
  .address { position: absolute; right: 112px; top: 452px; font-size: 22px; color: var(--ink); }
</style>
</head>
<body>
  <article class="card">
    <svg class="card-bands" viewBox="0 0 1050 600" aria-hidden="true">
      <polygon points="0,556 455,556 485,586 0,586" fill="var(--gray-light)"/>
      <polyline points="0,546 460,546" stroke="var(--blue)" stroke-width="4" fill="none"/>
      <polygon points="460,546 1050,478 1050,600 490,600 460,570" fill="var(--blue)"/>
    </svg>

    <div class="faint-mark" aria-hidden="true">
      <div class="square"></div>
      <div class="name">LEO<br>DART</div>
    </div>

    <header class="firm">
      <div class="circle"></div>
      <div>
        <div class="firm-name">LEO DART<small>PROFESSIONAL CORPORATION</small></div>
        <div class="credentials">Chartered Professional Accountant<br>Certified General Accountant</div>
      </div>
    </header>

    <div class="person">
      <div class="person-name">LEO DART</div>
      <div class="person-title">CPA, CGA</div>
    </div>

    <ul class="contacts">
      <li>(416) 555-0137
        <svg viewBox="0 0 26 22" aria-label="Telephone"><path d="M2 6c0-3 5-4 11-4s11 1 11 4v3h-6V6.5c-3-.8-7-.8-10 0V9H2z"/><path d="M7 10h12l4 10H3z"/></svg>
      </li>
      <li>(416) 555-0192
        <svg viewBox="0 0 26 22" aria-label="Fax"><rect x="7" y="1" width="12" height="6"/><rect x="1" y="8" width="24" height="9" rx="2"/><rect x="7" y="14" width="12" height="7"/></svg>
      </li>
      <li>leo@leodart.example
        <svg viewBox="0 0 26 22" aria-label="Email"><rect x="1" y="3" width="24" height="16"/><path d="M2 4l11 9 11-9" stroke="#fff" stroke-width="2" fill="none"/></svg>
      </li>
      <li>&nbsp;
        <svg viewBox="0 0 26 22" aria-label="Address"><path d="M13 1L1 11h3v10h7v-6h4v6h7V11h3z"/></svg>
      </li>
    </ul>
    <p class="address">47 Amberfield Cres. Richmond Hill, ON M3K 7P2</p>
  </article>
</body>
</html>
```